Journeys With Marcella Business Cards

I need a business card design for my upscale Travel Agency.
Attached you can find my logo.
I would like to include the following:
- Name
- Title
- Phone Number
- Email
- Website
- and then something like: Follow us: JourneysWithMarcella (and then social media icons in color).
The logo should be in the front and then also the back.
I am also attaching a design that I liked (mostly for the layout) but open to any suggestions
Industry/Entity Type
Travel Agent
Contact Information for Business Card
Name: Marcella Dorn
Title: Travel Designer / Owner
Phone: 415-927-3308
Email: marcella@journeyswithmarcella-example.com
Website: www.JourneysWithMarcella-example.com
Social Media Handles for FB,IG, Twitter: JourneysWithMarcella
Colors
Designer to choose colors to be used in the design.
Look and feel

```html
<!DOCTYPE html>
<html lang="en">
<head>
<meta charset="utf-8">
<title>Journeys With Marcella – Business Cards</title>
<link rel="stylesheet" href="https://fonts.googleapis.com/css2?family=Barlow:wght@400;600&display=swap">
<style>
  :root {
    --backdrop: #e4e0da;
    --card: #f3f3f3;
    --accent: #eca353;
    --ink: #2b2b2b;
    --on-accent: #ffffff;
  }
  * { box-sizing: border-box; margin: 0; padding: 0; }
  html, body { width: 900px; height: 1200px; overflow: hidden; }
  body {
    background: var(--backdrop);
    font-family: "Barlow", Arial, sans-serif;
    position: relative;
  }
  .card {
    position: absolute;
    left: 75px;
    width: 768px;
    background: var(--card);
    border-radius: 20px;
    overflow: hidden;
    box-shadow: 0 6px 14px rgba(0,0,0,0.25);
  }
  .card--front { top: 133px; height: 438px; }
  .card--back  { top: 627px; height: 441px; }

  .brush-band { position: absolute; left: 0; top: 0; width: 768px; }
  .card--front .brush-band { height: 438px; }
  .card--back .brush-band { height: 441px; }

  .monogram {
    position: absolute;
    color: var(--accent);
    font-weight: 600;
    line-height: 1;
    letter-spacing: 2px;
  }
  .card--front .monogram { left: 52px; top: 168px; font-size: 104px; }
  .card--back .monogram { left: 92px; top: 204px; font-size: 80px; }

  .identity { position: absolute; left: 362px; top: 122px; }
  .identity__name {
    color: var(--accent);
    font-size: 31px;
    font-weight: 600;
    letter-spacing: 2.5px;
    text-transform: uppercase;
    line-height: 1;
  }
  .identity__title { color: var(--ink); font-size: 22px; margin-top: 8px; }

  .contact-list { list-style: none; margin-top: 30px; }
  .contact-list li {
    display: flex; align-items: center;
    color: var(--ink);
    font-size: 18px;
    height: 31px;
    white-space: nowrap;
  }
  .contact-list svg { width: 18px; height: 18px; margin-right: 12px; fill: var(--accent); flex: none; }

  .wordmark-box {
    position: absolute;
    left: 288px; top: 178px;
    width: 374px; height: 115px;
    background: var(--accent);
    color: var(--on-accent);
    font-size: 32px;
    font-weight: 400;
    display: flex; align-items: center; justify-content: center;
    white-space: nowrap;
  }

  .follow {
    position: absolute;
    right: 35px; top: 35px;
    height: 44px;
    display: flex; align-items: center;
    color: var(--ink);
    font-size: 17px;
    white-space: nowrap;
  }
  .follow__handle { color: var(--accent); font-weight: 600; margin-left: 5px; }
  .follow__dot {
    width: 44px; height: 44px;
    border-radius: 50%;
    background: var(--accent);
    margin-left: 14px;
    flex: none;
  }
</style>
</head>
<body>

<section class="card card--front">
  <svg class="brush-band" viewBox="0 0 768 438" role="img" aria-label="Orange brush stroke sweeping across the lower right corner">
    <polygon points="370,438 430,410 560,385 768,330 768,438" fill="var(--accent)"/>
  </svg>

  <div class="monogram">JWM</div>

  <div class="identity">
    <h1 class="identity__name">Marcella Dorn</h1>
    <p class="identity__title">Travel Designer / Owner</p>
    <ul class="contact-list">
      <li>
        <svg viewBox="0 0 24 24"><path d="M3 9c0-3 4-5 9-5s9 2 9 5v2h-5V9H8v2H3zM6 12h12l2 8H4z"/></svg>
        415-927-3308
      </li>
      <li>
        <svg viewBox="0 0 24 24"><path d="M2 5h20v14H2z"/><path d="M3 6l9 7 9-7" fill="none" stroke="var(--card)" stroke-width="1.6"/></svg>
        marcella@journeyswithmarcella-example.com
      </li>
      <li>
        <svg viewBox="0 0 24 24"><g fill="none" stroke="var(--accent)" stroke-width="2"><circle cx="12" cy="12" r="9"/><ellipse cx="12" cy="12" rx="4" ry="9"/><path d="M3 12h18M5 7h14M5 17h14"/></g></svg>
        www.JourneysWithMarcella-example.com
      </li>
    </ul>
  </div>
</section>

<section class="card card--back">
  <svg class="brush-band" viewBox="0 0 768 441" role="img" aria-label="Orange brush stroke sweeping across the upper left corner">
    <polygon points="0,0 460,0 400,25 250,50 0,95" fill="var(--accent)"/>
  </svg>

  <p class="follow">Follow us:<span class="follow__handle">JourneysWithMarcella</span><span class="follow__dot" aria-hidden="true"></span></p>

  <div class="monogram">JWM</div>
  <div class="wordmark-box">Journeys With Marcella</div>
</section>

</body>
</html>
```